redesign corporate website (software courses)

We need a complete redesign of the current website: http://t-o-m.example/ (training: http://t-o-m.example/pt-br/treinamento/web ); more clear, different color, navigation, header, footer, whatever (side note: site will be based on bootstrap and drupal). Most important pages:

http://t-o-m.example/pt-br/treinamento (trainingoverviewpage)
http://t-o-m.example/ (frontpage)
http://t-o-m.example/pt-br/treinamento/web (trianingdetailpage)

The design should be valid for further content pages (like http://t-o-m.example/pt-br/desenvolvimentodesoftware) and pages with forms (http://t-o-m.example/pt-br/contact or http://t-o-m.example/pt-br/training/web/register)

Logo attached in white and black and black with shadow.

Some other examples of training sites (just content examples - not as template for similar layout):

http://www.brivatutor.example/packages/4817/Website-Development-Professional-training.html?advid=12&gclid=XQa93kLpr42DFbvn3BqeWTZBqk
http://www.kodewerk-kurse.example/
http://www.lumacod.example/cursos/quill-framework-ii/
http://www.travert-academy.example/lp/php-development-training.aspx?gclid=ZM3rhuPqx51DGTRR8Bpeyk9B2B

Industry/Entity Type

Software

```html
<!DOCTYPE html>
<html lang="en">
<head>
<meta charset="utf-8">
<title>Tech Orbit Masters – Software Training</title>
<link rel="stylesheet" href="https://fonts.googleapis.com/css2?family=Raleway:wght@400;500;600;700&display=swap">
<style>
:root{
  --orange:#f26522;
  --orange-soft:#f47b3c;
  --ink:#333333;
  --text:#555555;
  --muted:#8a8a8a;
  --page-grey:#efeff0;
  --band-grey:#f4f3f3;
  --white:#ffffff;
  --rule:#e3e3e3;
  --footer:#1e1e1e;
  --footer-bar:#2e2e2e;
  --date-dark:#5a5a5a;
}
*{box-sizing:border-box;margin:0;padding:0}
html,body{width:1200px;height:2177px;overflow:hidden}
body{font-family:'Raleway',sans-serif;color:var(--text);background:var(--white);position:relative}
.abs{position:absolute}

/* header */
.top{position:absolute;left:0;top:0;width:1200px;height:577px;background:linear-gradient(#ececed,#f4f4f5)}
.brand{position:absolute;display:flex;align-items:center;gap:8px;font-weight:700}
.brand-dot{width:30px;height:30px;border-radius:50%;background:var(--orange)}
.brand-name{font-size:30px;letter-spacing:1px}
.brand-sub{font-size:9px;line-height:10px;width:70px;text-transform:uppercase;letter-spacing:.5px}
.header-brand{left:135px;top:22px;color:var(--ink)}
.social-top{position:absolute;left:930px;top:24px;display:flex;gap:6px}
.social-top span{width:23px;height:23px;border-radius:50%;background:var(--white);border:1px solid #dcdcdc;display:block}
.nav{position:absolute;left:135px;top:74px;width:934px;height:39px;background:var(--white);border-radius:3px;box-shadow:0 2px 4px rgba(0,0,0,.08);display:flex;align-items:center;padding-left:19px}
.nav a{font-size:11px;color:var(--ink);text-decoration:none;text-transform:uppercase;padding:0 18px;border-left:1px solid #dedede;line-height:12px}
.nav a:first-child{border:none;padding-left:0;color:var(--orange)}

/* hero */
.hero{position:absolute;left:135px;top:142px;width:934px;height:410px;background:var(--white);padding:3px;box-shadow:0 1px 4px rgba(0,0,0,.12)}
.hero-photo{position:relative;width:100%;height:100%;background:linear-gradient(110deg,#2f3f55 0%,#8c9aae 30%,#c9c3b8 55%,#6b7a8e 80%,#3c4a5c 100%)}
.hero-caption{position:absolute;left:0;bottom:0;width:100%;height:128px;background:rgba(25,25,25,.78);padding:14px 20px}
.hero-caption h1{font-size:40px;font-weight:600;color:var(--white);letter-spacing:-.3px}
.hero-caption p{font-size:12.5px;color:#f0f0f0;width:670px;line-height:15px;margin-top:12px}
.hero-btn{position:absolute;right:36px;top:63px;width:141px;height:40px;border:2px solid var(--white);border-radius:3px;color:var(--white);font-size:16px;font-weight:600;display:flex;align-items:center;justify-content:center}

/* shared */
.section-title{font-size:18px;font-weight:600;color:var(--ink)}
.dotted{position:absolute;height:0;border-top:2px dotted var(--orange-soft)}
.btn{position:absolute;background:var(--orange);color:var(--white);font-size:11.5px;font-weight:600;display:flex;align-items:center;justify-content:center;border-radius:2px}

/* what we do */
.services-title{position:absolute;left:135px;top:608px;font-size:18px;font-weight:600;color:var(--orange)}
.services-rule{position:absolute;left:135px;top:640px;width:934px;border-top:1px solid var(--rule)}
.service{position:absolute;top:676px;width:220px}
.service-head{display:flex;align-items:center;gap:10px;font-size:14.5px;font-weight:500;color:var(--ink)}
.service-icon{width:26px;height:26px;border-radius:4px;background:var(--orange);display:flex;align-items:center;justify-content:center}
.service p{font-size:10.5px;line-height:13.5px;color:var(--muted);margin-top:21px}
.service .btn{position:relative;margin-top:30px;width:90px;height:27px}

/* about band */
.band{position:absolute;left:0;top:894px;width:1200px;height:402px;background:var(--band-grey)}
.about-intro{position:absolute;left:142px;top:989px;width:476px;font-size:12.5px;line-height:15px;color:var(--text)}
.about-photo{position:absolute;left:184px;top:1035px;width:119px;height:119px;background:linear-gradient(135deg,#5b4a42,#c2a99a 50%,#2f2b2b)}
.about-sub{position:absolute;left:316px;top:1033px;font-size:13px;font-weight:600;color:var(--ink)}
.about-side{position:absolute;left:316px;top:1055px;width:302px;font-size:11px;line-height:17.4px;color:var(--muted);text-align:justify}
.about-more{position:absolute;left:142px;top:1166px;width:476px;font-size:11px;line-height:17.4px;color:var(--muted);text-align:justify}
.quote{position:absolute;left:696px;width:367px;background:var(--white);padding:12px 16px;font-size:10.3px;line-height:17.4px;color:var(--text)}
.quote::after{content:"";position:absolute;left:52px;bottom:-9px;border-left:9px solid var(--white);border-bottom:9px solid transparent}
.quote-by{position:absolute;font-size:10.5px;font-weight:700;color:var(--ink)}
.pager{position:absolute;display:flex;gap:3px}
.pager span{width:14px;height:13px;display:flex;align-items:center;justify-content:center;font-size:10px;color:var(--white);line-height:1}
.pager .prev{background:#666}
.pager .next{background:var(--orange)}

/* blog + news */
.blog-photo{position:absolute;left:138px;top:1406px;width:471px;height:200px;background:linear-gradient(135deg,#e4d6bd,#cdb896 55%,#b9a582);border-bottom:3px solid var(--orange)}
.blog-date{position:absolute;left:136px;top:1630px;width:50px;color:var(--muted);font-weight:600;line-height:1}
.blog-date .m{font-size:13px;display:block}
.blog-date .d{font-size:24px;display:block}
.blog-divider{position:absolute;left:187px;top:1628px;height:86px;border-left:1px solid var(--rule)}
.blog-title{position:absolute;left:218px;top:1625px;font-size:19.5px;font-weight:500;color:var(--ink)}
.blog-meta{position:absolute;left:218px;top:1661px;font-size:10px;color:#b0b0b0}
.blog-excerpt{position:absolute;left:213px;top:1686px;width:400px;font-size:11px;line-height:18px;color:var(--muted)}
.blog-more{position:absolute;left:535px;top:1729px;font-size:11.5px;color:var(--ink);display:flex;align-items:center;gap:8px}
.news-item{position:absolute;left:694px;width:375px;display:flex;gap:12px;align-items:flex-start}
.news-date{width:32px;height:34px;border-radius:2px;background:var(--date-dark);color:var(--white);text-align:center;font-weight:700;line-height:1;padding-top:5px;flex:none}
.news-date.active{background:var(--orange)}
.news-date b{font-size:15px;display:block}
.news-date i{font-size:6px;font-style:normal;display:block;margin-top:1px}
.news-item p{font-size:11px;line-height:18px;color:var(--text);padding-top:0}
.news-item.active p{font-weight:700;color:var(--ink)}
.news-rule{position:absolute;left:694px;width:375px;border-top:2px dotted #9a9a9a}

/* footer */
.footer{position:absolute;left:0;top:1802px;width:1200px;height:335px;background:var(--footer);color:#e8e8e8}
.footer-bar{position:absolute;left:0;top:2137px;width:1200px;height:40px;background:var(--footer-bar);color:#cfcfcf;font-size:11px;display:flex;align-items:center;justify-content:center}
.footer-brand{left:144px;top:52px;color:var(--white)}
.footer-about{position:absolute;left:144px;top:120px;width:230px;font-size:11px;line-height:17.6px}
.footer-social{position:absolute;left:145px;top:235px;display:flex;gap:8px}
.footer-social span{width:30px;height:30px;border-radius:50%;background:#6a6a6a}
.footer-social span:first-child{background:var(--orange)}
.footer-head{position:absolute;top:48px;font-size:13px;font-weight:700;color:var(--white);text-transform:uppercase}
.footer-line{position:absolute;top:73px;border-top:1px solid #666}
.fn-date{position:absolute;left:464px;font-size:10px;color:var(--orange)}
.fn-text{position:absolute;left:464px;width:215px;font-size:10.5px;line-height:16px}
.field{position:absolute;left:800px;width:243px;background:var(--white);border-radius:4px;font-size:11px;color:#9a9a9a;display:flex;align-items:center;gap:10px;padding-left:14px}
.send{left:949px;top:276px;width:93px;height:32px;font-size:11px}
</style>
</head>
<body>

<div class="top"></div>

<header>
  <div class="brand header-brand">
    <span class="brand-dot"></span>
    <span class="brand-name">TOM</span>
    <span class="brand-sub">Tech Orbit Masters</span>
  </div>
  <div class="social-top" aria-label="Social links">
    <span></span><span></span><span></span><span></span><span></span>
  </div>
  <nav class="nav">
    <a href="#">Home</a><a href="#">Training</a><a href="#">About</a><a href="#">Contact</a>
  </nav>
</header>

<section class="hero">
  <div class="hero-photo" role="img" aria-label="Photo of trainees gathered around a laptop in a bright office">
    <div class="hero-caption">
      <h1>Grow Your Expertise</h1>
      <p>Take your career to the next level! TOM training and certification courses can get you where you want to go. The journey to a satisfying career as a TOM practitioner, Certified Lead Appraiser or TOM Instructor begins here</p>
      <div class="hero-btn">Read more</div>
    </div>
  </div>
</section>

<section class="services">
  <h2 class="services-title">What We Do</h2>
  <div class="services-rule"></div>

  <div class="service" style="left:135px">
    <div class="service-head"><span class="service-icon"><svg width="14" height="14" viewBox="0 0 14 14"><rect x="1" y="2" width="12" height="8" fill="none" stroke="#fff" stroke-width="1.6"/><rect x="5" y="11" width="4" height="1.6" fill="#fff"/></svg></span>Training</div>
    <p>We are privileged for being positioned in a region with IT ancestry. Therefore, from short courses to offer specializations to make it more</p>
    <div class="btn">Read more</div>
  </div>
  <div class="service" style="left:361px">
    <div class="service-head"><span class="service-icon"><svg width="14" height="14" viewBox="0 0 14 14"><circle cx="7" cy="7" r="4.4" fill="none" stroke="#fff" stroke-width="2.4" stroke-dasharray="2 1.45"/><circle cx="7" cy="7" r="1.6" fill="#fff"/></svg></span>Software Development</div>
    <p>We invest a lot in developing the quality and scalability combined with modern production tools. So the final product is more satisfactory and reliable.</p>
    <div class="btn">Read more</div>
  </div>
  <div class="service" style="left:605px">
    <div class="service-head"><span class="service-icon"><svg width="16" height="14" viewBox="0 0 16 14"><circle cx="5" cy="4" r="2.4" fill="#fff"/><circle cx="11" cy="4" r="2.4" fill="#fff"/><path d="M1 12c0-3 2-4.5 4-4.5s4 1.5 4 4.5zM7 12c0-3 2-4.5 4-4.5s4 1.5 4 4.5z" fill="#fff"/></svg></span>Consulting</div>
    <p>We work to improve the bond of the system with the processes of IT implementations always seeking leverage and minimize risks</p>
    <div class="btn">Read more</div>
  </div>
  <div class="service" style="left:855px">
    <div class="service-head"><span class="service-icon"><svg width="14" height="14" viewBox="0 0 14 14"><circle cx="7" cy="7" r="5.5" fill="none" stroke="#fff" stroke-width="1.6"/><path d="M1.5 7h11M7 1.5c-2.5 3-2.5 8 0 11M7 1.5c2.5 3 2.5 8 0 11" fill="none" stroke="#fff" stroke-width="1.1"/></svg></span>Course WEB</div>
    <p>Watch our calendar for more information on the course WEB , learn how the web environment works and how to get along across the labor market</p>
    <div class="btn">Read more</div>
  </div>
</section>

<section class="band">
  <h2 class="section-title abs" style="left:142px;top:30px">Get To Know Us a Little Better!</h2>
  <div class="dotted" style="left:142px;top:74px;width:476px"></div>
  <h2 class="section-title abs" style="left:694px;top:30px">What our Students have to say</h2>
  <div class="dotted" style="left:694px;top:74px;width:375px"></div>
</section>

<p class="about-intro">Pellentesque Aenean Vehicula Ullamcorper NibhNulla vitae libero, a pharetra augue. Donec sed odio dui. Cum sociis natoque penatibus et magnis.</p>
<div class="about-photo" role="img" aria-label="Photo of hands typing on laptops during a class"></div>
<h3 class="about-sub">Vestibulum Cras Tortor Ullamcorper</h3>
<p class="about-side">Nulla vitae elit libero, a pharetra augue. Curabitur blandit tempus porttitor. Cum sociis natoque penatibus et magnis dis parturient montes, nascetur ridiculus mus. Vivamus sagittis lacus vel augue laoreet rutrum faucibus dolor auctor. Sed posuere consectetur est at lobortis. Praesent commodo cursus magna, vel scelerisque nisl consectetur</p>
<p class="about-more">Nullam id dolor id nibh ultricies vehicula ut id elit. Lorem ipsum dolor sit amet, consectetur adipiscing elit. Aenean eu leo quam. Pellentesque ornare sem lacinia quam venenatis vestibulum. Donec sed odio dui. Maecenas faucibus mollis interdum.</p>
<div class="btn" style="left:528px;top:1228px;width:90px;height:27px">Read more</div>

<blockquote class="quote" style="top:990px;height:91px">Nullam quis risus eget urna mollis ornare vel eu leo. Maecenas faucibus mollis interdum. Nulla vitae elit libero, a pharetra augue. Aenean eu leo quam. Pellentesque ornare sem lacinia quam venenatis vestibulum. Integer posuere erat a ante venenatis.</blockquote>
<span class="quote-by" style="left:755px;top:1099px">by Rafe Dunmore</span>
<blockquote class="quote" style="top:1126px;height:75px">Praesent commodo cursus magna, vel scelerisque nisl consectetur et. Maecenas faucibus mollis interdum. Fusce dapibus, tellus ac cursus commodo, tortor mauris condimentum nibh.</blockquote>
<span class="quote-by" style="left:696px;top:1215px">by Corin Vale</span>
<div class="pager" style="left:1024px;top:1239px"><span class="prev">&lsaquo;</span><span class="next">&rsaquo;</span></div>

<section class="blog">
  <h2 class="section-title abs" style="left:138px;top:1330px">Latest from the blog</h2>
  <div class="pager" style="left:576px;top:1336px"><span class="prev">&lsaquo;</span><span class="next">&rsaquo;</span></div>
  <div class="dotted" style="left:138px;top:1367px;width:471px"></div>
  <div class="blog-photo" role="img" aria-label="Photo of a laptop, phone and notebook on a wooden desk"></div>
  <div class="blog-date"><span class="m">FEB</span><span class="d">08</span></div>
  <div class="blog-divider"></div>
  <h3 class="blog-title">Perspiciatis unde omnis iste natus error</h3>
  <p class="blog-meta">Posted by Lanterncraft | Street | 5 Comments</p>
  <p class="blog-excerpt">Sed ut perspiciatis unde omnis iste natus error sit voluptatem accusantium doloremque laudantium, totam rem...</p>
  <div class="blog-more"><svg width="10" height="10" viewBox="0 0 10 10"><path d="M1 5h7M5 2l3 3-3 3" fill="none" stroke="#f26522" stroke-width="1.4"/></svg>Read more</div>
</section>

<section class="news">
  <h2 class="section-title abs" style="left:694px;top:1332px">Recent News</h2>
  <div class="dotted" style="left:694px;top:1367px;width:375px"></div>

  <div class="news-item active" style="top:1403px"><span class="news-date active"><b>21</b><i>SEP</i></span><p>perspiciatis unde omnis iste natus error sit voluptatem accusantium</p></div>
  <div class="news-rule" style="top:1463px"></div>
  <div class="news-item" style="top:1480px"><span class="news-date"><b>20</b><i>SEP</i></span><p>perspiciatis unde omnis iste natus error sit voluptatem accusantium</p></div>
  <div class="news-rule" style="top:1539px"></div>
  <div class="news-item" style="top:1557px"><span class="news-date"><b>20</b><i>SEP</i></span><p>perspiciatis unde omnis iste natus error sit voluptatem accusantium</p></div>
  <div class="news-rule" style="top:1617px"></div>
  <div class="news-item" style="top:1638px"><span class="news-date"><b>20</b><i>SEP</i></span><p>perspiciatis unde omnis iste natus error sit voluptatem accusantium</p></div>
  <div class="news-rule" style="top:1694px"></div>
  <div class="btn" style="left:993px;top:1722px;width:75px;height:27px">See all</div>
</section>

<footer class="footer">
  <div class="brand footer-brand">
    <span class="brand-dot"></span>
    <span class="brand-name">TOM</span>
    <span class="brand-sub">Tech Orbit Masters</span>
  </div>
  <p class="footer-about">We are privileged for being positioned in a region with IT ancestry. Therefore, from short courses to offer specializations to make it more competitive with the labor market and train more competent professionals</p>
  <div class="footer-social" aria-label="Social links"><span></span><span></span><span></span></div>

  <h4 class="footer-head" style="left:464px">Recent News</h4>
  <div class="footer-line" style="left:464px;width:214px"></div>
  <span class="fn-date" style="top:101px">15.10.2013</span>
  <p class="fn-text" style="top:126px">Maecenas et nisl pellentesque, fermentum ante facilisis, aliquet ligula.</p>
  <span class="fn-date" style="top:174px">9.10.2013</span>
  <p class="fn-text" style="top:197px">Lorem ipsum dolor sit amet, consectetur adipiscing elit.</p>
  <span class="fn-date" style="top:245px">9.10.2013</span>
  <p class="fn-text" style="top:270px">Aliquam eu leo adipiscing, imperdiet arcunec, malesuada lorem.</p>

  <h4 class="footer-head" style="left:800px">Get in touch</h4>
  <div class="footer-line" style="left:800px;width:213px"></div>
  <div class="field" style="top:105px;height:31px"><svg width="10" height="10" viewBox="0 0 10 10"><circle cx="5" cy="3" r="2.2" fill="none" stroke="#aaa"/><path d="M1 9.5c0-2.5 2-3.5 4-3.5s4 1 4 3.5" fill="none" stroke="#aaa"/></svg>Full name</div>
  <div class="field" style="top:150px;height:31px"><svg width="11" height="9" viewBox="0 0 11 9"><rect x=".5" y=".5" width="10" height="8" fill="none" stroke="#aaa"/><path d="M.5 .5l5 4 5-4" fill="none" stroke="#aaa"/></svg>Email</div>
  <div class="field" style="top:195px;height:63px;align-items:flex-start;padding-top:12px"><svg width="11" height="10" viewBox="0 0 11 10"><path d="M1 1h9v6H4L1.5 9.5V7H1z" fill="none" stroke="#aaa"/></svg>Comments</div>
  <div class="btn send">SEND</div>
</footer>
<div class="footer-bar">©2014 Tech Orbit Masters</div>

</body>
</html>
```